MOON HARBOR SIGNAGE

Signage size 750mm x 6000mm long full colour.
Background please see pixelvault web site and see reference number 418 927 53
the text in the centre of the sign is to be in 3d bold script, to say
MOON HARBOR. Centre it and in slightly smaller text underneath write
PSYCHIC READINGS & HEALINGS
Then wherever best fits insert TEL: 8143 6097 and MOB: 0400 318 562

Keep the colours, heart and lines as similar as possible to the pixelvault image, you could try and reflaect the heart logo on the left and rignt hand side (IDEAS?)

I then have to duplicate the above on another sign 750mm high x 3000mm wide (ALL the signs are landscape)
text says the same, and same font as before MOON HARBOR and underneath centred slightly smaller PSYCHIC READINGS & HEALINGS

Try different layouts, for example you could also try PSYCHIC READINGS on top of each other centred and to the left, then stack PSYCHIC READINGS
&
HEALINGS

Target Market(s)

Anyone who wants Psychic readings...NOT KID orientated...Audience probably 25 and onwards

Industry/Entity Type

Landscape

Requirements
Must have
• See pixelvault heart and background as similar as you can

dimensions front sign 750mm x 6000mm

side sign 750mm x 3000mm

3d lettering, bold easy to read in contracsting colours to the background (See Pixelvault 418 92753 image)

```html
<!DOCTYPE html>
<html lang="en">
<head>
<meta charset="utf-8">
<title>Moon Harbor – Side Sign Proof</title>
<link rel="stylesheet" href="https://fonts.googleapis.com/css2?family=Arimo:wght@400;700&family=Dancing+Script:wght@700&display=swap">
<style>
  :root {
    --paper: #ffffff;
    --ink: #1a1a1a;
    --crop: #8a8a8a;
    --magenta-core: #d0147a;
    --magenta-mid: #9c0a55;
    --plum-edge: #2a0416;
    --night: #0d0208;
    --glow: #ff6fc0;
    --text-light: #ffffff;
  }
  * { margin: 0; padding: 0; box-sizing: border-box; }
  html, body {
    width: 1200px; height: 407px; overflow: hidden;
    background: var(--paper);
  }
  .proof {
    position: relative; width: 1200px; height: 407px;
    background: var(--paper);
    font-family: "Arimo", Arial, sans-serif;
  }
  .proof-specs {
    position: absolute; left: 84px; top: 6px;
    font-size: 13px; line-height: 17px; color: var(--ink);
    display: grid; grid-template-columns: auto auto; column-gap: 4px;
  }
  .crop-marks { position: absolute; inset: 0; }
  .crop-marks line { stroke: var(--crop); stroke-width: 1; }

  .sign {
    position: absolute; left: 72px; top: 71px;
    width: 1053px; height: 264px; overflow: hidden;
    background:
      radial-gradient(ellipse 48% 95% at 48% 40%, var(--magenta-core) 0%, var(--magenta-mid) 45%, var(--plum-edge) 80%, var(--night) 100%);
  }
  .sign-waves {
    position: absolute; top: 0; height: 100%;
  }
  .sign-waves--left {
    left: 0; width: 300px;
    background: linear-gradient(160deg, rgba(255,140,200,0.18) 0%, rgba(255,140,200,0) 55%);
  }
  .sign-waves--right {
    right: 0; width: 380px;
    background: linear-gradient(200deg, rgba(255,150,205,0.16) 0%, rgba(255,150,205,0) 50%),
                linear-gradient(340deg, rgba(255,150,205,0.22) 0%, rgba(255,150,205,0) 45%);
  }
  .sign-hearts {
    position: absolute; left: 80px; top: 20px;
    width: 260px; height: 190px; border-radius: 50%;
    background: radial-gradient(ellipse at 50% 50%, rgba(255,200,235,0.45) 0%, rgba(255,120,200,0.15) 45%, rgba(255,120,200,0) 72%);
  }
  .sign-name {
    position: absolute; left: 330px; top: 18px; width: 700px;
    text-align: center;
    font-family: "Dancing Script", cursive;
    font-weight: 700; font-size: 122px; line-height: 150px;
    color: var(--text-light);
    text-shadow: 0 0 6px var(--glow), 0 0 16px var(--glow), 0 0 32px rgba(255,80,170,0.8);
    white-space: nowrap;
  }
  .sign-services {
    position: absolute; left: 421px; top: 158px;
    font-size: 26px; color: var(--text-light);
    white-space: nowrap;
  }
  .sign-contact {
    position: absolute; right: 13px; bottom: 14px;
    font-size: 16.5px; font-weight: 700; color: var(--text-light);
    white-space: nowrap;
  }
</style>
</head>
<body>
<div class="proof">
  <div class="proof-specs">
    <span>Actual Size</span><span>: 3000mm x 750mm</span>
    <span>Artwork Size</span><span>: 300mm x 75mm</span>
  </div>

  <svg class="crop-marks" width="1200" height="407" viewBox="0 0 1200 407" aria-hidden="true">
    <line x1="72.5" y1="0" x2="72.5" y2="50"/>
    <line x1="1125.5" y1="0" x2="1125.5" y2="50"/>
    <line x1="72.5" y1="358" x2="72.5" y2="404"/>
    <line x1="1125.5" y1="358" x2="1125.5" y2="404"/>
    <line x1="0" y1="71.5" x2="50" y2="71.5"/>
    <line x1="0" y1="335.5" x2="50" y2="335.5"/>
    <line x1="1150" y1="71.5" x2="1200" y2="71.5"/>
    <line x1="1150" y1="335.5" x2="1200" y2="335.5"/>
  </svg>

  <section class="sign">
    <div class="sign-waves sign-waves--left" role="img" aria-label="Flowing fine pink wave lines with sparkles"></div>
    <div class="sign-waves sign-waves--right" role="img" aria-label="Flowing fine pink wave lines with sparkles"></div>
    <div class="sign-hearts" role="img" aria-label="Two glowing interlocking outline hearts"></div>
    <h1 class="sign-name">Moon Harbor</h1>
    <p class="sign-services">Psychic Readings &amp; Healings</p>
    <p class="sign-contact">TEL: 8143 6097 and MOB: 0400 318 562</p>
  </section>
</div>
</body>
</html>
```